Lantern Airfields Homepage Design Update

here's the current site - http://lanternairfields.example/

client is not happy with overall look.

keeping the same info - intro text, headlines, featured media excepts and general navigation options - can you come up with a nicer, slicker look for this homepage?

UPDATE: since it was asked by designer.. the general layout doesnt have to be the same. its not required to have a big image, with text below that and then smaller images/text below that. as long as we have the same content on the page, it can organized and designed in any way,

client like big images, so one way or the other, keep that... but feel free to reorganize content, explore different ways of framing it, and/or anything else. make this homepage pop!

for the designer that wins this, we'll start an additional project to update the interior.

let me know if any questions..

thanks!

marcus

Target Market(s)

aviation industry professionals, local governments, general public

Number of Pages Required

1 page

Font styles to use
Sans Serif

Requirements
Must have
• big image somewhere. same content as on current site, just designed differently.

```html
<!DOCTYPE html>
<html lang="en">
<head>
<meta charset="utf-8">
<title>Lantern Airfields – Home</title>
<link href="https://fonts.googleapis.com/css2?family=Saira:wght@400;500&family=Open+Sans:wght@400;600&display=swap" rel="stylesheet">
<style>
:root{
  --navy:#1d1b4c;
  --navy-light:#28266a;
  --ink:#333;
  --muted:#555;
  --top-grey:#d9d9d9;
  --footer:#2b2b2b;
  --footer-text:#9a9a9a;
  --line:#d0d0d0;
}
*{box-sizing:border-box;margin:0;padding:0}
html,body{width:1088px;height:1200px;overflow:hidden}
body{position:relative;background:#fff;font-family:"Open Sans",sans-serif;color:var(--ink)}
.abs{position:absolute}
.top-band{left:0;top:0;width:1088px;height:354px;background:var(--top-grey)}
.brand{left:88px;top:74px;display:flex;align-items:center;gap:14px}
.brand-dot{width:40px;height:40px;border-radius:50%;background:var(--navy)}
.brand-name{font-family:"Saira",sans-serif;font-weight:400;font-size:36px;color:var(--navy);letter-spacing:1px}
.contact{right:89px;text-align:right;font-size:10.5px;color:#333}
.contact.address{top:47px}
.contact.email{top:69px;color:var(--navy);text-decoration:underline}
.contact.phone{top:96px;font-size:14px;color:var(--navy);display:flex;align-items:center;gap:8px;font-family:"Saira",sans-serif}
.nav{left:90px;top:146px;width:908px;height:50px;background:linear-gradient(180deg,#25235f,#1a1846)}
.nav a{position:absolute;top:17px;color:#fff;text-decoration:none;font-family:"Saira",sans-serif;font-size:13px;letter-spacing:.3px}
.hero{left:90px;top:196px;width:908px;height:390px;background:linear-gradient(100deg,#2c5d98 0%,#5e8cc2 35%,#c9d6e4 60%,#eef0f3 75%,#d7dbe0 100%);box-shadow:0 14px 18px -10px rgba(0,0,0,.35)}
.hero-caption{left:0;top:102px;width:345px;height:191px;background:rgba(10,10,12,.88);color:#fff;padding:28px 30px}
.hero-caption h2{font-family:"Saira",sans-serif;font-weight:400;font-size:27px;letter-spacing:.5px}
.hero-caption p{margin-top:14px;font-size:11px;line-height:16px}
.btn{display:inline-block;background:linear-gradient(180deg,#2a2868,#17153f);color:#fff;border-radius:3px;text-decoration:none;font-family:"Saira",sans-serif}
.hero-caption .btn{margin-top:20px;font-size:10.5px;padding:7px 11px;font-family:"Open Sans",sans-serif}
.dots{left:425px;top:357px;display:flex;gap:12px}
.dots span{width:11px;height:11px;border-radius:50%;background:#9a9a9a}
.dots span.on{background:var(--navy)}
.welcome{left:0;top:630px;width:1088px;text-align:center}
.welcome h1{font-family:"Saira",sans-serif;font-weight:500;font-size:27px;color:var(--navy);letter-spacing:.5px}
.welcome p{width:900px;margin:14px auto 0;font-size:11.2px;line-height:18.5px;color:var(--muted)}
.welcome .btn{margin-top:24px;font-size:12px;padding:7px 16px}
.divider{left:0;top:827px;width:1088px;height:1px;background:var(--line)}
.featured{left:0;top:828px;width:1088px;height:287px;background:linear-gradient(180deg,#fcfcfc,#e9e9e9)}
.featured h2{position:absolute;left:88px;top:35px;font-family:"Saira",sans-serif;font-weight:500;font-size:27px;color:var(--navy)}
.arrow{top:38px;width:24px;height:26px;background:#1a1a1a;display:flex;align-items:center;justify-content:center}
.card{top:98px;width:445px;height:138px;background:#fff;border:1px solid var(--line)}
.card-photo{left:8px;top:8px;width:140px;height:119px}
.card-body{left:158px;top:6px;width:275px}
.card-body h3{font-family:"Saira",sans-serif;font-weight:400;font-size:13.6px;line-height:18.5px;color:var(--navy)}
.card-body time{display:block;margin-top:9px;font-size:11px;color:#222;padding-left:2px}
.card-body p{margin-top:8px;font-size:11px;line-height:18.5px;color:var(--muted);padding-left:2px}
.card-body a{font-size:11px;color:var(--navy);text-decoration:none;padding-left:3px}
.footer{left:0;top:1115px;width:1088px;height:85px;background:var(--footer)}
.footer-links{left:90px;top:27px;font-size:10.4px;color:var(--footer-text)}
.footer-links a{color:var(--footer-text);text-decoration:none}
.footer-links .sep{margin:0 8px}
.copyright{left:88px;top:48px;font-size:9.5px;color:var(--footer-text)}
.social{top:31px;width:28px;height:28px;background:#353535}
</style>
</head>
<body>
  <div class="abs top-band"></div>

  <header>
    <div class="abs brand">
      <span class="brand-dot"></span>
      <span class="brand-name">Lantern Airfields</span>
    </div>
    <div class="abs contact address">410 Harbor Lane, 12th Floor, Eastport, NY 10099</div>
    <div class="abs contact email">info@lanternairfields.example</div>
    <div class="abs contact phone">
      <svg width="12" height="12" viewBox="0 0 12 12"><rect width="12" height="12" rx="2" fill="#1d1b4c"/><path d="M3.5 2.8c.4-.3.8-.2 1 .2l.6 1.2c.1.3 0 .6-.2.8l-.4.3c.4.9 1 1.5 1.9 1.9l.3-.4c.2-.2.5-.3.8-.2l1.2.6c.4.2.5.6.2 1-.6.8-1.4 1-2.3.6C4.9 8 3.9 7 3.2 5.4c-.4-.9-.3-1.9.3-2.6z" fill="#fff"/></svg>
      (555) 014-3098
    </div>
  </header>

  <nav class="abs nav">
    <a style="left:29px">ABOUT</a>
    <a style="left:132px">SERVICES</a>
    <a style="left:251px">AIRPORTS</a>
    <a style="left:372px">NEWS &amp; MEDIA</a>
    <a style="left:528px">CONTACT</a>
    <a style="left:645px">EMPLOYEES</a>
  </nav>

  <section class="abs hero" role="img" aria-label="Close view of a white passenger jet's nose and engine against a blue sky">
    <div class="abs hero-caption">
      <h2>Bringing private</h2>
      <p>Fixed Based Operators (FBOs) and also related non-aeronautical uses such as hotels,</p>
      <a class="btn">Read More</a>
    </div>
    <div class="abs dots"><span></span><span class="on"></span><span></span></div>
  </section>

  <section class="abs welcome">
    <h1>WELCOME TO LANTERNAIRFIELDS</h1>
    <p>Lantern Airfields is focused on opportunities to invest, develop and manage both general aviation and commercial service airports in key U.S. markets. A subsidiary of Lantern Investments, a private equity firm that exclusively invests in the Aerospace &amp; Transportation sectors, Lantern has the resources available to invest and finance transactions. Lantern maintains offices in New York, Dublin and Atlanta.</p>
    <a class="btn">Read More</a>
  </section>

  <div class="abs divider"></div>

  <section class="abs featured">
    <h2>FEATURED MEDIA</h2>
    <div class="abs arrow" style="left:950px"><svg width="8" height="8" viewBox="0 0 8 8"><path d="M5.5 1 2.5 4l3 3" stroke="#fff" fill="none" stroke-width="1.3"/></svg></div>
    <div class="abs arrow" style="left:975px"><svg width="8" height="8" viewBox="0 0 8 8"><path d="M2.5 1l3 3-3 3" stroke="#fff" fill="none" stroke-width="1.3"/></svg></div>

    <article class="abs card" style="left:90px">
      <div class="abs card-photo" role="img" aria-label="Close-up of a radial aircraft engine in sepia tones" style="background:radial-gradient(circle at 55% 50%,#3a342c 0%,#7a6f60 45%,#b9ad9a 100%)"></div>
      <div class="abs card-body">
        <h3>Lantern Airfields to Develop Passenger Terminal at Harbor Field</h3>
        <time>March 3, 2015</time>
        <p>Lantern Airfields a developer of passenger terminals and airport support facilities...</p>
        <a>Read More</a>
      </div>
    </article>

    <article class="abs card" style="left:553px">
      <div class="abs card-photo" role="img" aria-label="Propeller aircraft flying head-on under cloudy sky" style="background:radial-gradient(circle at 50% 50%,#c8ccd2 0%,#7c8795 45%,#3c4654 100%)"></div>
      <div class="abs card-body">
        <h3>Lantern Airfields to Develop Passenger Terminal at Harbor Field</h3>
        <time>March 3, 2015</time>
        <p>Lantern Airfields a developer of passenger terminals and airport support facilities...</p>
        <a>Read More</a>
      </div>
    </article>
  </section>

  <footer class="abs footer">
    <div class="abs footer-links">
      <a>Home</a><span class="sep">I</span><a>Services</a><span class="sep">I</span><a>Airports</a><span class="sep">I</span><a>News &amp; Media</a><span class="sep">I</span><a>Contact</a><span class="sep">I</span><a>Employees</a>
    </div>
    <div class="abs copyright">© 2015 lanternairfields.example. All rights reserved.</div>
    <span class="abs social" style="left:833px"></span>
    <span class="abs social" style="left:867px"></span>
    <span class="abs social" style="left:901px"></span>
    <span class="abs social" style="left:935px"></span>
    <span class="abs social" style="left:969px"></span>
  </footer>
</body>
</html>
```